UK Supplement Company Needs a Label for Diet Protein Powder

We need a new, modern and fresh design for our Diet Protein Powder. Our protein powder is packaged in black plastic tubs (photo attached) and needs an attractive label. We would like to see designs that grab attention and look professional. We're very open to ideas. The label should be 88mm x 365mm. We also prefer PSD format where possible. These alterations could be made once your design is chosen. Have attached photo of our shake ingredients/benefits.
Updates

Need extra days to review

Target Market(s)

Slimmers

Industry/Entity Type

Health And Wellness

Font styles to use
Serif
Sans Serif

Colors

Designer to choose colors to be used in the design.

Requirements
Must have
• Clean, Modern and Professional Look. Eye catching. The flavour, we offer 6 flavours so this must be something we can edit (Flavours are Banana, Chocolate, Chocolate Mint, Strawberry, Toffee and Vanilla).
Nice to have
• Our logo, this can be KELVO Nutrition or just KELVO. Our logo files are attached.
Should not have
• We do not want to see people (faces or bodies) on the design.

```html
<!DOCTYPE html>
<html lang="en">
<head>
<meta charset="utf-8">
<title>KELVO Nutrition – Diet Protein Powder Label</title>
<link href="https://fonts.googleapis.com/css2?family=Montserrat:wght@700&family=Josefin+Sans:wght@400;600&display=swap" rel="stylesheet">
<style>
  :root {
    --tub-black: #1f1f21;
    --band-blue: #3ea4dc;
    --band-blue-light: #5cb8ea;
    --brand-blue: #4fb6ea;
    --choc-dark: #3a231d;
    --choc-mid: #4e2c24;
    --lime: #cfe24b;
    --lime-text: #c9dd45;
    --ink-dark: #2a2418;
  }
  html, body {
    margin: 0;
    padding: 0;
    width: 1200px;
    height: 960px;
    overflow: hidden;
    background: var(--tub-black);
  }
  .label {
    position: relative;
    width: 1200px;
    height: 960px;
    background: var(--tub-black);
  }
  .label__band {
    position: absolute;
    left: 0;
    top: 60px;
    width: 1200px;
    height: 780px;
    background: linear-gradient(90deg, var(--band-blue) 0%, var(--band-blue-light) 50%, var(--band-blue) 100%);
  }
  .label__accent {
    position: absolute;
    bottom: 120px;
    width: 0;
    height: 0;
  }
  .label__accent--left {
    left: 0;
    border-bottom: 70px solid var(--lime);
    border-right: 90px solid transparent;
  }
  .label__accent--right {
    right: 0;
    border-bottom: 70px solid var(--lime);
    border-left: 90px solid transparent;
  }
  .panel {
    position: absolute;
    left: 310px;
    top: 60px;
    width: 580px;
    height: 760px;
    border-radius: 0 0 48px 48px;
    background: linear-gradient(180deg, var(--choc-mid) 0%, var(--choc-dark) 100%);
    display: flex;
    flex-direction: column;
    align-items: center;
  }
  .brand {
    margin-top: 92px;
    display: flex;
    flex-direction: column;
    align-items: center;
    font-family: "Montserrat", sans-serif;
    font-weight: 700;
  }
  .brand__name {
    font-size: 124px;
    line-height: 1;
    letter-spacing: -2px;
    color: var(--brand-blue);
  }
  .brand__sub {
    margin-top: 12px;
    font-size: 22px;
    letter-spacing: 15px;
    padding-left: 15px;
    color: var(--lime-text);
  }
  .product-name {
    margin: 30px 0 0;
    font-family: "Josefin Sans", sans-serif;
    font-weight: 600;
    font-size: 72px;
    line-height: 1.04;
    text-align: center;
    color: var(--lime-text);
  }
  .flavour {
    margin-top: 18px;
    width: 380px;
    padding: 6px 0 3px;
    background: var(--lime);
    color: var(--ink-dark);
    font-family: "Josefin Sans", sans-serif;
    font-weight: 400;
    font-size: 26px;
    text-align: center;
  }
  .flavour-image {
    margin-top: 42px;
    width: 400px;
    height: 150px;
    border-radius: 40px;
    background: radial-gradient(ellipse at center, #b48468 0%, #8a5a43 45%, rgba(78,44,36,0) 75%);
  }
</style>
</head>
<body>
  <main class="label">
    <div class="label__band"></div>
    <div class="label__accent label__accent--left"></div>
    <div class="label__accent label__accent--right"></div>
    <section class="panel">
      <div class="brand">
        <span class="brand__name">KELVO</span>
        <span class="brand__sub">NUTRITION</span>
      </div>
      <h1 class="product-name">DIET PROTEIN<br>POWDER</h1>
      <div class="flavour">CHOCOLATE FLAV</div>
      <div class="flavour-image" role="img" aria-label="Broken pieces of milk chocolate"></div>
    </section>
  </main>
</body>
</html>
```